Harvest Fresh Wonders (Postcard)

Looking for a professional post card (5x7) - front and back, graphic design to promote a campaign called Harvest Fresh Wonders. The goal is to promote Orthodontics in our dental practice for our existing and new patients.

```html
<!DOCTYPE html>
<html lang="en">
<head>
<meta charset="utf-8">
<title>Harvest Fresh Wonders – Postcard</title>
<link rel="stylesheet" href="https://fonts.googleapis.com/css2?family=Poppins:wght@300;400;500;600;700;800&family=Arimo:wght@400;700&display=swap">
<style>
  :root{
    --stage:#2b2b2b;
    --paper:#ffffff;
    --paper-tint:#f7f5f2;
    --navy:#123a73;
    --navy-deep:#0d3068;
    --orange:#e8781f;
    --orange-light:#f4a640;
    --gold:#f7b52c;
    --gold-deep:#eda11a;
    --ink:#3a3a3a;
    --bullet-bg:#fbe3c6;
  }
  *{box-sizing:border-box;margin:0;padding:0}
  html,body{width:1200px;height:1137px;overflow:hidden;background:var(--stage)}
  body{position:relative;font-family:"Poppins",sans-serif}
  .card{position:absolute;left:236px;width:732px;background:var(--paper);overflow:hidden}
  .card--front{top:33px;height:525px}
  .card--back{top:579px;height:523px}
  .pattern-field{position:absolute;inset:0;background:linear-gradient(180deg,#fff 0%,var(--paper-tint) 100%)}
  .brand{position:absolute;left:0;right:0;display:flex;justify-content:center;align-items:center;gap:10px}
  .brand__dot{width:20px;height:20px;border-radius:50%;background:var(--orange)}
  .brand__name{font-weight:600;font-size:27px;color:var(--navy);letter-spacing:1px;line-height:1}
  .front__brand{top:27px}
  .front__title{position:absolute;top:78px;left:0;right:0;text-align:center;font-weight:700;font-size:47px;
    color:var(--orange);letter-spacing:0.5px;line-height:1}
  .front__offer{position:absolute;top:130px;left:0;right:0;display:flex;justify-content:center;align-items:center;gap:8px;
    font-weight:600;font-size:25px;color:var(--navy)}
  .burst{position:relative;display:flex;align-items:center;justify-content:center}
  .burst svg{position:absolute;inset:0}
  .burst__text{position:relative;text-align:center;line-height:1;font-weight:700}
  .burst__amount{display:block}
  .burst__label{display:block;font-weight:600}
  .front__burst{width:86px;height:86px}
  .front__burst .burst__amount{font-size:26px;color:var(--navy)}
  .front__burst .burst__label{font-size:13px;color:var(--navy)}
  .front__photo{position:absolute;left:102px;top:208px;width:502px;height:252px;
    background:radial-gradient(ellipse at 50% 40%,#8a5a3f 0%,#b98b6d 45%,rgba(240,225,210,0) 75%)}
  .swoosh{position:absolute;left:0;width:732px}
  .pill{position:absolute;height:32px;border-radius:16px;background:var(--navy-deep);color:#fff;
    font-weight:600;font-size:17px;display:flex;align-items:center;justify-content:center}
  .front__pill{left:152px;width:433px;top:454px}
  .contact{position:absolute;left:0;right:0;display:flex;justify-content:center;align-items:center;
    font-size:16px;color:var(--ink)}
  .contact__item{display:flex;align-items:center;gap:8px}
  .contact__sep{width:1px;height:16px;background:var(--orange);margin:0 14px}
  .contact__icon{width:22px;height:22px}
  .front__contact{top:495px}
  /* back */
  .back__band{position:absolute;left:0;top:0;width:732px;height:153px;
    background:linear-gradient(90deg,var(--orange) 0%,var(--orange-light) 100%)}
  .back__photo{position:absolute;left:0;top:0;width:266px;height:153px;
    background:linear-gradient(180deg,#e9c3b6 0%,#d98f86 55%,#f1d7cf 100%)}
  .back__title{position:absolute;left:278px;top:34px;color:#fff;line-height:1.05;text-align:center;width:310px}
  .back__title-strong{display:block;font-weight:700;font-size:36px}
  .back__title-light{display:block;font-weight:300;font-size:42px}
  .postage{position:absolute;left:598px;top:18px;width:122px;height:121px;background:#fff;border:1px solid #333;
    font-family:"Arimo",sans-serif;font-size:15px;color:#222;text-align:center;display:flex;flex-direction:column;
    justify-content:center;line-height:1.3}
  .postage strong{font-weight:700}
  .back__pill-offer{position:absolute;left:130px;top:174px;width:267px;height:62px;border-radius:0 31px 31px 0;
    background:linear-gradient(90deg,var(--orange-light),var(--gold));color:#fff;font-weight:600;font-size:21px;
    line-height:1.15;display:flex;align-items:center;justify-content:center;padding-left:40px;text-align:center}
  .back__burst{position:absolute;left:44px;top:142px;width:124px;height:124px}
  .back__burst .burst__amount{font-size:30px;color:#fff}
  .back__burst .burst__label{font-size:17px;color:#fff}
  .address{position:absolute;left:417px;top:163px;width:306px;height:103px;border:1.5px solid #333;background:#fff;
    padding:34px 0 0 22px;font-weight:600;font-size:15px;color:#111;line-height:1.3}
  .back__copy{position:absolute;left:20px;top:277px;width:380px;font-size:15.5px;line-height:1.22;color:var(--ink)}
  .features{position:absolute;left:413px;top:282px;width:319px;height:68px;background:var(--bullet-bg);
    border-left:3px solid var(--orange);padding:4px 0 0 18px;list-style:none;color:var(--navy);font-weight:600;
    font-size:15.5px;line-height:1.25}
  .features__item::before{content:"• "}
  .features__sub{padding-left:12px}
  .back__brand{top:408px}
  .back__pill{left:151px;width:433px;top:453px}
  .back__contact{top:492px}
</style>
</head>
<body>

<section class="card card--front">
  <div class="pattern-field" role="img" aria-label="Faint pattern of tooth and dental care icons"></div>
  <div class="brand front__brand"><span class="brand__dot"></span><span class="brand__name">Brightway Dental</span></div>
  <h1 class="front__title">HARVEST FRESH WONDERS</h1>
  <div class="front__offer">
    <span>Enjoy</span>
    <div class="burst front__burst">
      <svg viewBox="0 0 100 100"><g fill="var(--gold)"><rect x="18" y="18" width="64" height="64"/><rect x="18" y="18" width="64" height="64" transform="rotate(30 50 50)"/><rect x="18" y="18" width="64" height="64" transform="rotate(60 50 50)"/></g><circle cx="50" cy="50" r="38" fill="var(--gold-deep)" opacity=".35"/></svg>
      <div class="burst__text"><span class="burst__amount">$500</span><span class="burst__label">Savings</span></div>
    </div>
    <span>Orthodontic Treatment</span>
  </div>
  <div class="front__photo" role="img" aria-label="Photo of three smiling teenage girls, one wearing braces"></div>
  <svg class="swoosh" style="top:370px" width="732" height="90" viewBox="0 0 732 90">
    <path d="M0 0 Q90 55 170 84 L170 90 Q80 65 0 34 Z" fill="var(--orange)"/>
    <path d="M732 0 Q642 55 562 84 L562 90 Q652 65 732 34 Z" fill="var(--orange)"/>
  </svg>
  <div class="pill front__pill">Now Offering Braces for Your Best Smile</div>
  <div class="contact front__contact">
    <span class="contact__item"><svg class="contact__icon" viewBox="0 0 22 22"><circle cx="11" cy="11" r="11" fill="var(--orange)"/><path d="M7.5 6.5l2 2-1 1.2c.6 1.4 1.6 2.4 3 3l1.2-1 2 2-1.2 1.4c-3.5-.4-6.8-3.7-7.2-7.2z" fill="#fff"/></svg>844-555-0142</span>
    <span class="contact__sep"></span>
    <span class="contact__item"><svg class="contact__icon" viewBox="0 0 22 22"><circle cx="11" cy="11" r="11" fill="var(--orange)"/><rect x="6" y="7.5" width="10" height="7" fill="#fff"/><path d="M6 7.5l5 4 5-4" stroke="var(--orange)" fill="none"/></svg>hello@brightwaydental.health</span>
    <span class="contact__sep"></span>
    <span class="contact__item"><svg class="contact__icon" viewBox="0 0 22 22"><circle cx="11" cy="11" r="11" fill="var(--orange)"/><circle cx="11" cy="11" r="5.5" fill="none" stroke="#fff" stroke-width="1.4"/><path d="M5.5 11h11M11 5.5c-2.5 3-2.5 8 0 11M11 5.5c2.5 3 2.5 8 0 11" stroke="#fff" fill="none"/></svg>brightwaydental.com</span>
  </div>
</section>

<section class="card card--back">
  <div class="pattern-field" role="img" aria-label="Faint pattern of tooth and dental care icons"></div>
  <div class="back__band"></div>
  <div class="back__photo" role="img" aria-label="Close-up photo of a smile, half with braces and half with straight teeth"></div>
  <h2 class="back__title"><span class="back__title-strong">HARVEST FRESH</span><span class="back__title-light">WONDERS</span></h2>
  <div class="postage">PRSRT STD<br>ECRWSS<br>U.S. POSTAGE<br><strong>PAID</strong>EDDM RETAIL</div>
  <div class="back__pill-offer">Orthodontic<br>Treatment</div>
  <div class="burst back__burst">
    <svg viewBox="0 0 100 100"><g fill="var(--gold)"><rect x="18" y="18" width="64" height="64"/><rect x="18" y="18" width="64" height="64" transform="rotate(22.5 50 50)"/><rect x="18" y="18" width="64" height="64" transform="rotate(45 50 50)"/><rect x="18" y="18" width="64" height="64" transform="rotate(67.5 50 50)"/></g><circle cx="50" cy="50" r="36" fill="var(--gold-deep)"/></svg>
    <div class="burst__text"><span class="burst__amount">$500</span><span class="burst__label">Savings</span></div>
  </div>
  <div class="address">Local<br>Postal Customer</div>
  <p class="back__copy">We offer a range of orthodontic services to fit your individual needs, including Orvane. Orvane is a popular alternative to traditional braces that uses clear aligners to gradually straighten your teeth.</p>
  <ul class="features">
    <li class="features__item">Braces</li>
    <li class="features__sub">(metal / ceramic / clear)</li>
    <li class="features__item">Flexible payment plans</li>
  </ul>
  <svg class="swoosh" style="top:366px" width="732" height="90" viewBox="0 0 732 90">
    <path d="M0 0 Q90 55 170 84 L170 90 Q80 65 0 34 Z" fill="var(--orange)"/>
    <path d="M732 0 Q642 55 562 84 L562 90 Q652 65 732 34 Z" fill="var(--orange)"/>
  </svg>
  <div class="brand back__brand"><span class="brand__dot"></span><span class="brand__name">Brightway Dental</span></div>
  <div class="pill back__pill">Call Today to Schedule or Free Consultation</div>
  <div class="contact back__contact">
    <span class="contact__item"><svg class="contact__icon" viewBox="0 0 22 22"><circle cx="11" cy="11" r="11" fill="var(--orange)"/><path d="M7.5 6.5l2 2-1 1.2c.6 1.4 1.6 2.4 3 3l1.2-1 2 2-1.2 1.4c-3.5-.4-6.8-3.7-7.2-7.2z" fill="#fff"/></svg>844-555-0142</span>
    <span class="contact__sep"></span>
    <span class="contact__item"><svg class="contact__icon" viewBox="0 0 22 22"><circle cx="11" cy="11" r="11" fill="var(--orange)"/><rect x="6" y="7.5" width="10" height="7" fill="#fff"/><path d="M6 7.5l5 4 5-4" stroke="var(--orange)" fill="none"/></svg>hello@brightwaydental.health</span>
    <span class="contact__sep"></span>
    <span class="contact__item"><svg class="contact__icon" viewBox="0 0 22 22"><circle cx="11" cy="11" r="11" fill="var(--orange)"/><circle cx="11" cy="11" r="5.5" fill="none" stroke="#fff" stroke-width="1.4"/><path d="M5.5 11h11M11 5.5c-2.5 3-2.5 8 0 11M11 5.5c2.5 3 2.5 8 0 11" stroke="#fff" fill="none"/></svg>brightwaydental.com</span>
  </div>
</section>

</body>
</html>
```